KVD INDUSTRIES TOMB CARD DESIGN

KVD Industries
Prineville Office: 2284 SW Hollister Rd, Prineville, OR 97754
Redmond Office: 4718 NW 47th Street, Redmond, OR 97756
Serving continuous Process Industries Since 1981
Manufacturing, Welding, machining, Design, Reverse Engineering

Welding

Contact Information for Business Card

Tom Bristow
CEO/TECHNICAL ANALYST
Phone: 1-541-555-0142
DIRECT LINE: 1-541-555-0187
Cell No 1-541-555-0163

```html
<!DOCTYPE html>
<html lang="en">
<head>
<meta charset="utf-8">
<title>KVD Industries – Business Card</title>
<link rel="stylesheet" href="https://fonts.googleapis.com/css2?family=Montserrat:wght@600;700&family=Open+Sans:wght@400&family=Arimo:wght@400&display=swap">
<style>
  :root {
    --bg: #e9e6e1;
    --card-white: #ffffff;
    --navy: #0b0b3b;
    --brand-blue: #3a3f93;
    --title-yellow: #f2e400;
    --text-white: #ffffff;
  }
  html, body {
    margin: 0;
    padding: 0;
    width: 1200px;
    height: 1200px;
    overflow: hidden;
    background: var(--bg);
  }
  .canvas {
    position: relative;
    width: 1200px;
    height: 1200px;
  }
  .business-card {
    position: absolute;
    left: 100px;
    top: 314px;
    width: 1000px;
    height: 572px;
    background: var(--card-white);
    overflow: hidden;
    box-shadow: 0 12px 30px rgba(0,0,0,0.18);
  }
  .card-wave {
    position: absolute;
    inset: 0;
    width: 100%;
    height: 100%;
  }
  .brand {
    position: absolute;
    left: 70px;
    top: 92px;
    display: flex;
    align-items: center;
    gap: 16px;
  }
  .brand-square {
    width: 58px;
    height: 58px;
    background: var(--brand-blue);
  }
  .brand-name {
    font-family: "Montserrat", sans-serif;
    font-weight: 700;
    font-size: 38px;
    letter-spacing: 1px;
    color: var(--brand-blue);
    text-transform: uppercase;
  }
  .person {
    position: absolute;
    left: 62px;
    top: 332px;
    width: 300px;
  }
  .person-name {
    font-family: "Montserrat", sans-serif;
    font-weight: 700;
    font-size: 35px;
    color: var(--text-white);
    margin: 0;
    letter-spacing: 0.3px;
    white-space: nowrap;
  }
  .person-title {
    font-family: "Open Sans", sans-serif;
    font-size: 19px;
    color: var(--title-yellow);
    margin: 4px 0 0;
    white-space: nowrap;
  }
  .divider {
    position: absolute;
    left: 402px;
    top: 292px;
    width: 3px;
    height: 124px;
    background: var(--text-white);
  }
  .contact-list {
    position: absolute;
    left: 470px;
    top: 282px;
    margin: 0;
    padding: 0;
    list-style: none;
    font-family: "Arimo", sans-serif;
    font-size: 26px;
    line-height: 40px;
    color: var(--text-white);
    white-space: nowrap;
  }
  .services {
    position: absolute;
    left: 160px;
    bottom: 44px;
    margin: 0;
    font-family: "Open Sans", sans-serif;
    font-size: 20px;
    color: var(--text-white);
    white-space: nowrap;
  }
</style>
</head>
<body>
<main class="canvas">
  <article class="business-card">
    <svg class="card-wave" viewBox="0 0 1000 572" preserveAspectRatio="none" aria-hidden="true">
      <path fill="var(--navy)" d="M0,268 C170,305 330,300 470,200 C600,105 690,25 800,0 L1000,0 L1000,572 L0,572 Z"/>
    </svg>

    <div class="brand">
      <span class="brand-square"></span>
      <span class="brand-name">KVD Industries</span>
    </div>

    <div class="person">
      <h1 class="person-name">TOM BRISTOW</h1>
      <p class="person-title">CEO/TECHNICAL ANALYST</p>
    </div>

    <span class="divider"></span>

    <ul class="contact-list">
      <li>Phone : 1-541-555-0142</li>
      <li>Direct Line : 1-541-555-0187</li>
      <li>Cell No : 1-541-555-0163</li>
    </ul>

    <p class="services">Manufacturing, Welding, machining, Design, Reverse Engineering</p>
  </article>
</main>
</body>
</html>
```